Real Estate Investment Company Needs A Business Card Designed

I need a business card designed for my use. We are a real estate investment company based in Omaha, Nebraska that specializes in buying, rehabbing and selling single family and multifamily properties. Would love designs that incorporate our logo and colors

Industry/Entity Type

Business

Contact Information for Business Card

Mitchell Parkhurst | President & CEO
4873 North 52nd Avenue, Ste 700
Omaha, NE 68142
(402) 786-4259
mitchell@kestrelgateproperties.example
www.KestrelgateProperties.example

Font styles to use
Serif

Colors
0255a3
3276b5

Requirements
Must have
• Our logo

```html
<!DOCTYPE html>
<html lang="en">
<head>
<meta charset="utf-8">
<title>Kestrelgate Properties – Business Card</title>
<link rel="stylesheet" href="https://fonts.googleapis.com/css2?family=Questrial&display=swap">
<style>
  :root {
    --page-bg: #e9e6e1;
    --card-dark: #3d4045;
    --card-dark-edge: #33363a;
    --card-white: #ffffff;
    --brand-blue: #0255a3;
    --brand-blue-light: #3276b5;
    --text-light: #e4e6e8;
    --text-muted: #c3c6ca;
    --divider: #8a8e93;
  }
  * { box-sizing: border-box; margin: 0; padding: 0; }
  html, body {
    width: 1200px; height: 800px; overflow: hidden;
    background: var(--page-bg);
    font-family: "Questrial", "Century Gothic", sans-serif;
  }
  .stage {
    position: relative; width: 1200px; height: 800px;
    display: flex; align-items: center; justify-content: center; gap: 40px;
  }
  .card {
    position: relative; width: 540px; height: 309px; overflow: hidden;
    border-radius: 3px;
    box-shadow: 0 10px 28px rgba(0,0,0,.18);
  }

  /* Back of card */
  .card-back {
    background: var(--card-dark);
    display: flex; align-items: center; justify-content: center;
  }
  .card-back .brand { flex-direction: column; gap: 10px; }
  .card-back .brand-mark { width: 46px; height: 46px; }
  .card-back .brand-name { font-size: 26px; color: var(--brand-blue-light); }

  /* Shared brand lockup */
  .brand { display: flex; align-items: center; }
  .brand-mark {
    border-radius: 50%;
    background: var(--brand-blue);
  }
  .brand-name {
    letter-spacing: 1.5px; text-transform: uppercase;
    text-align: center; line-height: 1.1;
  }

  /* Front of card */
  .card-front { background: var(--card-dark); }
  .front-top {
    position: absolute; left: 0; top: 0; width: 100%; height: 150px;
    background: var(--card-white);
    display: flex; align-items: center; justify-content: center;
  }
  .front-top .brand { flex-direction: column; gap: 8px; }
  .front-top .brand-mark { width: 40px; height: 40px; }
  .front-top .brand-name { font-size: 22px; color: var(--brand-blue); }
  .accent-band {
    position: absolute; left: 0; top: 150px; width: 100%; height: 6px;
    background: var(--brand-blue-light);
    border-bottom: 2px solid var(--card-white);
  }

  .front-info {
    position: absolute; left: 0; top: 158px; width: 100%; height: 151px;
    display: flex; align-items: center;
  }
  .person {
    width: 240px; padding-right: 18px; text-align: right;
  }
  .person-name { font-size: 17px; color: var(--brand-blue-light); }
  .person-title { margin-top: 5px; font-size: 12.5px; color: var(--text-light); }
  .divider { width: 1px; height: 104px; background: var(--divider); }
  .contact { padding-left: 14px; list-style: none; }
  .contact li {
    display: flex; align-items: flex-start; gap: 7px;
    font-size: 10.5px; line-height: 1.45; color: var(--text-light);
  }
  .contact .icon {
    flex: none; width: 11px; height: 11px; margin-top: 2px;
    fill: var(--brand-blue-light);
  }
</style>
</head>
<body>
<main class="stage">

  <section class="card card-back" aria-label="Business card, back">
    <div class="brand">
      <span class="brand-mark"></span>
      <span class="brand-name">Kestrelgate Properties</span>
    </div>
  </section>

  <section class="card card-front" aria-label="Business card, front">
    <div class="front-top">
      <div class="brand">
        <span class="brand-mark"></span>
        <span class="brand-name">Kestrelgate Properties</span>
      </div>
    </div>
    <div class="accent-band"></div>

    <div class="front-info">
      <div class="person">
        <p class="person-name">Mitchell Parkhurst</p>
        <p class="person-title">President &amp; CEO</p>
      </div>
      <div class="divider"></div>
      <ul class="contact">
        <li>
          <svg class="icon" viewBox="0 0 24 24" aria-hidden="true"><path d="M6.6 10.8a15.1 15.1 0 0 0 6.6 6.6l2.2-2.2a1 1 0 0 1 1-.25 11.4 11.4 0 0 0 3.6.57 1 1 0 0 1 1 1V20a1 1 0 0 1-1 1A17 17 0 0 1 3 4a1 1 0 0 1 1-1h3.5a1 1 0 0 1 1 1c0 1.25.2 2.45.57 3.57a1 1 0 0 1-.25 1z"/></svg>
          <span>(402) 786-4259</span>
        </li>
        <li>
          <svg class="icon" viewBox="0 0 24 24" aria-hidden="true"><path d="M2 5h20v14H2z M4 7v.5l8 5 8-5V7z" fill-rule="evenodd"/></svg>
          <span>mitchell@kestrelgateproperties.example</span>
        </li>
        <li>
          <svg class="icon" viewBox="0 0 24 24" aria-hidden="true"><path d="M12 2a10 10 0 1 0 0 20 10 10 0 0 0 0-20zm6.9 6h-3a15.6 15.6 0 0 0-1.4-3.6A8 8 0 0 1 18.9 8zM12 4c.8 1.2 1.5 2.5 1.9 4h-3.8c.4-1.5 1.1-2.8 1.9-4zM4.3 14a8 8 0 0 1 0-4h3.4a16 16 0 0 0 0 4zm.8 2h3a15.6 15.6 0 0 0 1.4 3.6A8 8 0 0 1 5.1 16zm3-8h-3a8 8 0 0 1 4.4-3.6A15.6 15.6 0 0 0 8.1 8zM12 20c-.8-1.2-1.5-2.5-1.9-4h3.8c-.4 1.5-1.1 2.8-1.9 4zm2.3-6H9.7a14.7 14.7 0 0 1 0-4h4.6a14.7 14.7 0 0 1 0 4zm.2 5.6a15.6 15.6 0 0 0 1.4-3.6h3a8 8 0 0 1-4.4 3.6zm1.8-5.6a16 16 0 0 0 0-4h3.4a8 8 0 0 1 0 4z"/></svg>
          <span>www.KestrelgateProperties.example</span>
        </li>
        <li>
          <svg class="icon" viewBox="0 0 24 24" aria-hidden="true"><path d="M12 2a7 7 0 0 0-7 7c0 5.2 7 13 7 13s7-7.8 7-13a7 7 0 0 0-7-7zm0 9.5A2.5 2.5 0 1 1 12 6.5a2.5 2.5 0 0 1 0 5z"/></svg>
          <span>4873 North 52nd Avenue, Ste 700<br>Omaha, NE 68142</span>
        </li>
      </ul>
    </div>
  </section>

</main>
</body>
</html>
```